Lumo-Grid Business Card Design

We are an Managed IT Services provider, our main aim is to support business IT outsourcing, we provide these services: Network Services ,Technical Support , In House IT Services , Server Solutions , Anti-Spam , Online backup , Brellix Desk Suite ,Work from Home Solutions , IT Planning & Installation.

Target Market(s)

Information Technology

Industry/Entity Type

Business

Contact Information for Business Card

Lumo-Grid, Inc.12103 Sailboat WayCooper City, FL 33026Phone: 305-720-7162Email: support@lumo-grid.com

Font styles to use
Serif

Requirements
Must have
• a nice logo

```html
<!DOCTYPE html>
<html lang="en">
<head>
<meta charset="utf-8">
<title>Lumo-Grid Business Card</title>
<link rel="stylesheet" href="https://fonts.googleapis.com/css2?family=Cinzel:wght@500&family=Tinos&display=swap">
<style>
  :root {
    --ink: #0b0c0d;
    --card-top: #1b1d1f;
    --card-edge: #090a0b;
    --gold: #d9a92a;
    --gold-light: #f3d35a;
    --gold-deep: #b5811a;
    --text: #f4f4f2;
    --tile-haze: rgba(255,255,255,0.045);
  }
  * { margin: 0; padding: 0; box-sizing: border-box; }
  html, body { width: 1025px; height: 1200px; overflow: hidden; background: var(--ink); }
  .sheet { position: relative; width: 1025px; height: 1200px; background: var(--ink); }
  .card {
    position: absolute; left: 0; width: 1025px;
    background: radial-gradient(ellipse at 50% 45%, var(--card-top) 0%, var(--card-edge) 80%);
    overflow: hidden;
  }
  .card-front { top: 0; height: 572px; }
  .card-back { top: 598px; height: 574px; }
  .gold-band {
    position: absolute; left: 0; width: 1025px; height: 18px;
    background: linear-gradient(90deg, var(--gold-deep), var(--gold-light) 20%, var(--gold) 45%, var(--gold-light) 70%, var(--gold-deep));
  }
  .band-front { top: 572px; }
  .band-back { top: 1172px; }
  .brand-name {
    position: absolute; left: 0; width: 100%; text-align: center;
    font-family: "Cinzel", serif; font-weight: 500; color: var(--gold);
    letter-spacing: 2px; line-height: 1;
  }
  .brand-front { top: 250px; font-size: 84px; }
  .brand-back { top: 222px; font-size: 70px; }
  .tile-haze { position: absolute; }
  .haze-upper { left: 0; top: 0; width: 1025px; height: 200px;
    background: radial-gradient(ellipse 70% 100% at 40% 0%, var(--tile-haze), transparent 100%); }
  .haze-corner { right: 0; top: 280px; width: 360px; height: 294px;
    background: radial-gradient(ellipse at 80% 50%, var(--tile-haze), transparent 70%); }
  .contact {
    position: absolute; display: flex; align-items: center; gap: 12px;
    font-family: "Tinos", serif; font-size: 25px; color: var(--text); white-space: nowrap;
  }
  .contact svg { width: 40px; height: 40px; flex: none; }
  .contact-address { left: 150px; top: 436px; }
  .contact-email { left: 148px; top: 495px; }
  .contact-phone { left: 543px; top: 495px; }
</style>
</head>
<body>
<div class="sheet">
  <section class="card card-front">
    <div class="brand-name brand-front">Lumo-Grid</div>
  </section>
  <div class="gold-band band-front"></div>

  <section class="card card-back">
    <div class="tile-haze haze-upper" role="img" aria-label="Faint pattern of scattered dark squares"></div>
    <div class="tile-haze haze-corner" role="img" aria-label="Faint grid of dark squares"></div>
    <div class="brand-name brand-back">Lumo-Grid</div>

    <div class="contact contact-address">
      <svg viewBox="0 0 40 40" aria-hidden="true">
        <path d="M4 20 L20 6 L36 20 Z" fill="var(--gold)"/>
        <rect x="9" y="19" width="22" height="17" fill="var(--gold)"/>
        <rect x="13" y="23" width="5" height="5" fill="var(--ink)"/>
        <rect x="22" y="25" width="5" height="11" fill="var(--ink)"/>
      </svg>
      <span>Lumo-Grid, Inc.48217 Heron Crest LaneAlder Bay, NC 33981</span>
    </div>

    <div class="contact contact-email">
      <svg viewBox="0 0 40 40" aria-hidden="true">
        <rect x="2" y="8" width="36" height="24" fill="var(--gold)"/>
        <path d="M2 8 L20 22 L38 8 M2 32 L15 18 M38 32 L25 18" stroke="var(--ink)" stroke-width="2" fill="none"/>
      </svg>
      <span>Email: support@lumo-grid.com</span>
    </div>

    <div class="contact contact-phone">
      <svg viewBox="0 0 40 40" aria-hidden="true">
        <rect x="1" y="1" width="38" height="38" rx="8" fill="var(--gold)"/>
        <path d="M12 9 L16 9 L18 15 L15 17 Q18 23 23 25 L25 22 L31 24 L31 28 Q30 31 26 31 Q12 28 9 13 Q9 9 12 9 Z" fill="var(--ink)"/>
      </svg>
      <span>Phone: 727-418-9253</span>
    </div>
  </section>
  <div class="gold-band band-back"></div>
</div>
</body>
</html>
```